Geschäftspapiere für Autohaus
Zielgruppe
Wir sind ein Autohaus mit zwei Standorten wo wir an dem einen Standort die Marke Velko & an dem anderen Tavik und Quorel haben.
Aufgabenstellung
Wir möchten ein modernes, frisches Design für unser Briefpapier sowie Verkaufsmappen haben. Das aktuelle Briefpapier sowie die Verkaufsmappen haben wir angehängt. Das neue Design sollte auf jeden Fall unser Firmenlogo sowie das jeweilige Markenlogo (Velko, Tavik oder Quorel) enthalten. Die Adresse sollte im Kopfbereich aufgeführt werden und alle Angaben wie Bankverbindung etc. in der Fußzeile. Sonst haben wir vom Design keine weiteren Vorgaben, auch nicht bei der Verkaufsmappe. Wir möchten die Sachen über Drucklotse drucken lassen. Eine Layoutvorlage für die Verkaufsmappen sind beigefügt.

```html
<!DOCTYPE html>
<html lang="de">
<head>
<meta charset="utf-8">
<title>Brandt &amp; Kowalski – Briefpapier und Verkaufsmappe</title>
<link rel="stylesheet" href="https://fonts.googleapis.com/css2?family=Inter:wght@700&family=Lato:wght@300;400;700&display=swap">
<style>
:root{
  --bg:#efefef;
  --blue:#1570b8;
  --navy:#0e4a80;
  --ink:#333333;
  --grey:#8a8a8a;
  --soft:#f4f3f3;
  --white:#ffffff;
}
*{margin:0;padding:0;box-sizing:border-box}
html,body{width:1200px;height:1133px;overflow:hidden;background:var(--bg)}
body{position:relative;font-family:"Lato",sans-serif;color:var(--ink)}
.section-title{position:absolute;top:178px;font-family:"Inter",sans-serif;font-weight:700;font-size:32px;letter-spacing:.2px;color:var(--blue)}
.section-title.letter-title{left:103px}
.section-title.folder-title{left:600px}

/* Briefpapier */
.letterhead{position:absolute;left:103px;top:235px;width:439px;height:621px;background:var(--white);box-shadow:0 20px 30px rgba(0,0,0,.10)}
.letterhead .abs{position:absolute}
.rule{position:absolute;left:26px;width:388px;height:1px;background:var(--blue)}
.group-bar{left:26px;top:29px;width:224px;height:18px;background:var(--blue);color:var(--white);font-size:8.2px;font-weight:700;line-height:18px;padding-left:12px;letter-spacing:.1px}
.bar-divider{left:255px;top:29px;width:1px;height:16px;background:#bbb}
.brand-row{left:266px;top:32px;width:148px;display:flex;justify-content:space-between}
.brand-row .brand{position:relative;font-size:6.4px;font-weight:700;letter-spacing:1px;color:var(--ink);display:flex;align-items:center;gap:3px}
.brand .dot-mark{width:6px;height:6px;border:1px solid var(--ink);border-radius:50%}
.brand-row .brand::after{content:"";position:absolute;left:50%;top:13px;width:3px;height:3px;margin-left:-1px;border-radius:50%;background:var(--blue)}
.company-mark{left:26px;top:69px;width:108px}
.company-mark .name{font-size:11.5px;font-weight:700;color:var(--blue);white-space:nowrap;letter-spacing:-.2px}
.company-mark .sub{margin-top:3px;font-size:5.6px;letter-spacing:4.3px;color:var(--grey)}
.mark-divider{left:140px;top:57px;width:1px;height:48px;background:var(--blue)}
.dealer-box{left:149px;top:57px;width:266px;height:46px;background:var(--soft)}
.dealer-box .label{position:absolute;left:11px;top:9px;font-size:6.2px;font-weight:700;color:var(--ink)}
.dealer-box .label b{color:var(--blue)}
.dealer-box .col{position:absolute;top:20px;font-size:5.8px;line-height:9px;color:var(--grey);font-weight:300}
.dealer-box .col.c1{left:11px}
.dealer-box .col.c2{left:94px}
.dealer-box .brand-tag{position:absolute;right:12px;top:10px;display:flex;flex-direction:column;align-items:center;gap:3px;font-size:6.8px;font-weight:700;letter-spacing:1.2px;color:#111}
.brand-tag .dot-mark{width:16px;height:16px;border:1.5px solid #111;border-radius:50%}
.recipient{left:46px;top:154px;font-size:6.3px;line-height:10.4px}
.recipient .to{font-size:8px;line-height:11px}
.recipient .who{font-size:8.6px;font-weight:700;color:var(--blue);line-height:12px}
.date{left:330px;top:154px;font-size:6.3px}
.body-copy{left:46px;top:240px;width:350px;font-size:6.5px;line-height:14.5px}
.body-copy p{margin-bottom:14.5px}
.signature{left:46px;top:420px;width:92px;height:26px;background:linear-gradient(90deg,#f3f3f3,#e6e6e6)}
.signer{left:46px;top:448px;font-size:8.6px;line-height:11px}
.signer span{display:block;font-size:6.3px}
.footer-legal{left:26px;top:518px;width:118px;font-size:4.6px;line-height:6.3px;color:#222}
.footer-divider{position:absolute;width:1px;background:var(--blue)}
.footer-reg{left:161px;top:518px;font-size:4.6px;line-height:6.3px;color:var(--grey);font-weight:300}
.footer-rule{left:26px;top:549px;width:268px;height:1px;background:var(--blue)}
.footer-bank{top:561px;font-size:4.6px;line-height:6.3px;color:var(--grey);font-weight:300}
.slogan-box{left:298px;top:520px;width:116px;height:58px;background:var(--soft);border:1px solid #ececec;display:flex;align-items:center;justify-content:center;font-size:11px;font-weight:300;letter-spacing:1px;color:var(--grey);font-style:italic}
.base-band{left:26px;top:609px;width:388px;height:12px;background:var(--blue)}

/* Verkaufsmappe */
.sales-folder{position:absolute;left:601px;top:235px;width:495px;height:698px;background:var(--blue);box-shadow:0 22px 34px rgba(0,0,0,.12);color:var(--white)}
.folder-mark{position:absolute;left:96px;top:298px;width:303px;text-align:center}
.folder-mark .name{font-size:34px;font-weight:700;line-height:40px;white-space:nowrap;letter-spacing:-.5px}
.folder-mark .line{height:1.5px;background:var(--white);margin:5px 0 6px}
.folder-mark .sub{font-size:18px;font-weight:700;letter-spacing:15px;margin-right:-15px}
.brand-strip{position:absolute;left:73px;top:411px;width:349px;height:43px;border-top:1px solid rgba(255,255,255,.7);border-bottom:1px solid rgba(255,255,255,.7)}
.brand-strip .inner{position:absolute;left:0;right:0;top:4px;height:34px;background:var(--navy);display:flex;align-items:center;justify-content:space-around;padding:0 8px}
.brand-strip .brand{display:flex;align-items:center;gap:7px;font-size:13px;letter-spacing:2.6px;font-weight:400}
.brand-strip .dot-mark{width:17px;height:17px;border:1.5px solid var(--white);border-radius:50%}
</style>
</head>
<body>
<h1 class="section-title letter-title">BRIEFPAPIER</h1>
<h1 class="section-title folder-title">VERKAUFSMAPPE</h1>

<section class="letterhead" aria-label="Briefpapier">
  <div class="rule" style="top:25px"></div>
  <div class="abs group-bar">UNTERNEHMENSGRUPPE BRANDT &amp; KOWALSKI</div>
  <div class="abs bar-divider"></div>
  <div class="abs brand-row">
    <span class="brand"><i class="dot-mark"></i>VELKO</span>
    <span class="brand"><i class="dot-mark"></i>TAVIK</span>
    <span class="brand"><i class="dot-mark"></i>QUOREL</span>
  </div>
  <div class="rule" style="top:51px"></div>

  <div class="abs company-mark">
    <div class="name">BRANDT &amp; KOWALSKI</div>
    <div class="sub">AUTOHÄUSER</div>
  </div>
  <div class="abs mark-divider"></div>
  <div class="abs dealer-box">
    <div class="label"><b>VELKO</b>-VERTRAGSHÄNDLER</div>
    <div class="col c1">Telefon: 0381-77 64 20<br>Telefax: 0381-77 64 299</div>
    <div class="col c2">info.velko@bk-autohaus.de<br>www.bk-autohaus.de</div>
    <div class="brand-tag"><i class="dot-mark"></i>VELKO</div>
  </div>
  <div class="rule" style="top:113px"></div>

  <div class="abs recipient">
    <div class="to">TO</div>
    <div class="who">JEAN DOE</div>
    Chief Director<br>
    <span style="display:block;margin-top:2px">City, Road Name - 12345</span>
    Email@company.com<br>
    +00 000 0000
  </div>
  <div class="abs date">Date: 10 April, 2020</div>

  <div class="abs body-copy">
    <p>Lorem ipsum dolor sit amet, consectetur adipiscing elit, sed do eiusmod tempor incididunt ut labore et dolore magna aliqua. Ut enim ad minim veniam, quis nostrud exercitation ullamco laboris nisi ut aliquip ex ea commodo consequat. Duis aute irure dolor in reprehenderit in voluptate velit esse cillum dolore eu fugiat nulla pariatur. Excepteur sint occaecat cupidatat non proident, sunt in culpa qui officia deserunt mollit anim id est laborum.</p>
    <p>Sed ut perspiciatis unde omnis iste natus error sit voluptatem accusantium doloremque l audantium, totam rem aperiam, eaque ipsa quae ab illo inventore veritatis et quasi architecto beatae vitae dicta sunt explicabo Neque eius modi tempora incidunt ut labore et dolore magnam aliquam quaerat voluptatem.</p>
    <p>Ut enim ad minima veniam, quis nostrum exercitationem ullam corporis suscipit laboriosam, nisi ut aliquid ex ea commodi consequatur. Quis autem vel eum iure reprehenderit qui in ea voluptate velit esse quam nihil</p>
  </div>

  <div class="abs signature" role="img" aria-label="Handschriftliche Unterschrift"></div>
  <div class="abs signer">Lena Hartwig<span>Chief Director</span></div>

  <div class="rule" style="top:511px"></div>
  <div class="abs footer-legal">Aufträge führen wir nur aus gemäß „Bedingungen für die Ausführung von Arbeiten an Kraftfahrzeugen, Anhängern und deren Teilen und für Kostenvoranschläge“ (siehe Aushang).</div>
  <div class="footer-divider" style="left:150px;top:516px;height:26px"></div>
  <div class="abs footer-reg">Eingetragen Registergericht Warnemark Nr. HRB 4417<br>St.-Nr.: 080/112/05531 · Ust-ID-Nr.: DE 200417733<br>Geschäftsführer: Jonas Brandt</div>
  <div class="abs footer-rule"></div>
  <div class="abs footer-bank" style="left:26px">Bankverbindungen<br>Nordbank Seenland eG<br>Küstenbank Mitte eG</div>
  <div class="footer-divider" style="left:124px;top:557px;height:24px"></div>
  <div class="abs footer-bank" style="left:134px">BIC: NORDDEF1XXX<br>BIC: KUESDEF1XXX</div>
  <div class="footer-divider" style="left:188px;top:557px;height:24px"></div>
  <div class="abs footer-bank" style="left:197px">IBAN: DE12 3456 7890 1234 5678 90<br>IBAN: DE98 7654 3210 9876 5432 10</div>
  <div class="abs slogan-box">fahrfreude</div>
  <div class="rule" style="top:586px"></div>
  <div class="abs base-band"></div>
</section>

<section class="sales-folder" aria-label="Verkaufsmappe">
  <div class="folder-mark">
    <div class="name">BRANDT &amp; KOWALSKI</div>
    <div class="line"></div>
    <div class="sub">AUTOHÄUSER</div>
  </div>
  <div class="brand-strip">
    <div class="inner">
      <span class="brand"><i class="dot-mark"></i>VELKO</span>
      <span class="brand"><i class="dot-mark"></i>TAVIK</span>
      <span class="brand"><i class="dot-mark"></i>QUOREL</span>
    </div>
  </div>
</section>
</body>
</html>
```